BUSINESS CARD MIRELLE CAVANOSI

I need a new business card for my personal business.
I am a Naturopath and Nutritionist working doing private consults in the health and wellness arena.
I would like to see designs that are, clean minimalist but colourful.
I like:
White (clean,fresh, minimalist)
pops of one colour ONLY.Choose a colour to run with and keep it simple.
green
light blue
mustard
Bright yellow
Charcoal
The final design should communicate professionalism but also be in touch with nature.
Key Information to include:
MIRELLE CAVANOSI
ABN 48 217 603 915
RQTLBE 327081
Tel 0487 639 142
NATUROPATH | HERBALIST | NUTRITON CONSULTANT
BHSc (Naturopathic Studies) Grad Dip (Naturopathy)
BACK OF CARD : YOUR NEXT APPOINTMENT ..................................
I already have a logo (picture attached)But I would be more than happy to NOT have this included. I am very Open to cards WITHOUT current logo/ ones that weave the colour of my logo but do not use the logo.
I have included pictures attached to give examples of the styles/colors I enjoy.
Updates
I have added a picture of a mortar and pestle - one just like this would be lovely to include in your entry.
TIA

```html
<!DOCTYPE html>
<html lang="en">
<head>
<meta charset="utf-8">
<title>Mirelle Cavanosi Naturopath – Business Card</title>
<link rel="stylesheet" href="https://fonts.googleapis.com/css2?family=Antonio:wght@400&family=Questrial&display=swap">
<style>
  :root {
    --canvas: #ecefe8;
    --green-deep: #5c8f2e;
    --green-mid: #6da636;
    --green-light: #7bb440;
    --leaf-pale: rgba(220, 236, 200, 0.75);
    --card-white: #f6f8f2;
    --card-mist: #e6eedc;
    --ink: #55585a;
    --accent: #6f9a2c;
    --white: #ffffff;
  }
  * { box-sizing: border-box; margin: 0; padding: 0; }
  html, body {
    width: 1200px;
    height: 1000px;
    overflow: hidden;
    background: var(--canvas);
  }
  .card {
    position: absolute;
    border-radius: 30px;
    overflow: hidden;
    box-shadow: 0 4px 14px rgba(0, 0, 0, 0.18);
  }

  /* Front */
  .card-front {
    left: 208px; top: 35px; width: 794px; height: 457px;
    background: radial-gradient(ellipse at 45% 40%, var(--green-light) 0%, var(--green-mid) 45%, var(--green-deep) 100%);
  }
  .front-foliage {
    position: absolute;
    left: 0; top: 0; width: 300px; height: 457px;
    background: linear-gradient(90deg, rgba(200, 228, 170, 0.35) 0%, rgba(200, 228, 170, 0.15) 60%, rgba(200, 228, 170, 0) 100%);
  }
  .front-leaf {
    position: absolute;
    left: 452px; top: 110px; width: 334px; height: 343px;
    background: radial-gradient(ellipse at 50% 55%, var(--leaf-pale) 0%, rgba(200, 225, 170, 0.6) 65%, rgba(200, 225, 170, 0) 72%);
  }
  .front-title {
    position: absolute;
    left: 477px; top: 302px;
  }
  .front-title text {
    font-family: "Antonio", "Arial Narrow", sans-serif;
    fill: var(--white);
    font-size: 40px;
  }

  /* Back */
  .card-back {
    left: 210px; top: 503px; width: 793px; height: 457px;
    background: linear-gradient(120deg, var(--card-mist) 0%, var(--card-white) 55%, var(--white) 100%);
  }
  .back-foliage {
    position: absolute;
    left: 0; top: 0; width: 560px; height: 457px;
    background: radial-gradient(ellipse at 35% 45%, rgba(200, 216, 185, 0.45) 0%, rgba(220, 232, 210, 0.2) 60%, rgba(255, 255, 255, 0) 85%);
  }
  .back-vine {
    position: absolute;
    right: 0; top: 0; width: 290px; height: 457px;
    background: linear-gradient(270deg, rgba(150, 190, 110, 0.55) 0%, rgba(170, 205, 135, 0.35) 55%, rgba(200, 225, 175, 0) 100%);
  }
  .back-details {
    position: absolute;
    left: 86px; top: 92px;
    font-family: "Questrial", "Century Gothic", sans-serif;
    color: var(--ink);
  }
  .practitioner-name {
    font-size: 26px;
    font-weight: 400;
    letter-spacing: 0.2px;
    line-height: 1;
  }
  .practitioner-name .role { color: var(--accent); }
  .modalities, .qualifications {
    font-size: 16.5px;
    line-height: 1;
  }
  .modalities { margin-top: 18px; }
  .qualifications { margin-top: 9px; }

  .contact {
    position: absolute;
    left: 90px; top: 324px;
    font-family: "Questrial", "Century Gothic", sans-serif;
    color: var(--ink);
    list-style: none;
  }
  .contact li {
    display: flex;
    align-items: center;
    font-size: 19px;
    line-height: 26px;
  }
  .contact svg { margin-right: 6px; }
  .registration {
    position: absolute;
    left: 91px; top: 377px;
    font-family: "Questrial", "Century Gothic", sans-serif;
    color: var(--ink);
    font-size: 16px;
    line-height: 22px;
  }
  .registration .label { color: var(--accent); }
</style>
</head>
<body>

<section class="card card-front" aria-label="Front of card">
  <div class="front-foliage" role="img" aria-label="Faint climbing leaves along the left edge"></div>
  <div class="front-leaf" role="img" aria-label="Large pale veined leaf behind the name"></div>
  <svg class="front-title" width="300" height="110" viewBox="0 0 300 110" aria-label="Mirelle Cavanosi Naturopathy">
    <text x="0" y="38" textLength="282" lengthAdjust="spacingAndGlyphs">MIRELLE CAVANOSI</text>
    <text x="0" y="84" textLength="282" lengthAdjust="spacing">NATUROPATHY</text>
  </svg>
</section>

<section class="card card-back" aria-label="Back of card">
  <div class="back-foliage" role="img" aria-label="Soft translucent leaves in the background"></div>
  <div class="back-vine" role="img" aria-label="Green leafy vine along the right edge"></div>

  <div class="back-details">
    <h1 class="practitioner-name">MIRELLE CAVANOSI <span class="role">NATUROPATH</span></h1>
    <p class="modalities">NATUROPATH | HERBALIST | NUTRITON CONSULTANT</p>
    <p class="qualifications">BHSc (Naturopathic Studies) Grad Dip (Naturopathy)</p>
  </div>

  <ul class="contact">
    <li>
      <svg width="20" height="20" viewBox="0 0 20 20" aria-hidden="true">
        <circle cx="10" cy="10" r="9.5" fill="#6f9a2c"/>
        <rect x="7" y="4.5" width="6" height="11" rx="1.2" fill="none" stroke="#fff" stroke-width="1.3"/>
        <rect x="8.3" y="6" width="3.4" height="5" fill="#fff"/>
      </svg>
      12345678910
    </li>
    <li>
      <svg width="20" height="20" viewBox="0 0 20 20" aria-hidden="true">
        <circle cx="10" cy="10" r="9.5" fill="#6f9a2c"/>
        <rect x="5" y="6.5" width="10" height="7" rx="0.8" fill="#fff"/>
        <path d="M5 6.8 L10 10.6 L15 6.8" fill="none" stroke="#6f9a2c" stroke-width="1.2"/>
      </svg>
      youremail@here.com
    </li>
  </ul>

  <p class="registration">
    <span class="label">ABN</span> 48 217 603 915<br>
    <span class="label">RQTLBE</span> 327081
  </p>
</section>

</body>
</html>
```